Business card for law firm

Need business card for new law firm. Think confident, authoritative, conservative, but not stuffy or old-fashioned.

Contact Information for Business Card

Content for card - logo (uploaded), plus the following:

Paul Wexbury (larger font)
Managing Partner (larger font, but not as large as name)
Level 9, 41 Tansy Lane
Sydney NSW 2000
Main Tel 02 7346 2190
Direct Tel 02 6273 4415
Email paul@qvlegal.com.au
www.qvlegal.com.au

Letterhead design should include logo plus:
Level 9, 41 Tansy Lane
Sydney NSW 2000
Tel 02 6273 4415
www.qvlegal.com.au

```html
<!DOCTYPE html>
<html lang="en">
<head>
<meta charset="utf-8">
<title>Quayvale Lawyers – Business Card</title>
<link rel="stylesheet" href="https://fonts.googleapis.com/css2?family=Spectral:wght@500&family=Lato:wght@400&family=Montserrat:wght@400&display=swap">
<style>
  :root {
    --navy: #1b2457;
    --grey: #4a4a4a;
    --card: #fbfbfb;
    --backdrop: #e4e4e6;
  }
  * { margin: 0; padding: 0; box-sizing: border-box; }
  html, body {
    width: 1200px;
    height: 1200px;
    overflow: hidden;
    background: var(--backdrop);
  }
  .card {
    position: absolute;
    left: 166px;
    top: 353px;
    width: 867px;
    height: 494px;
    background: var(--card);
    border-radius: 4px;
    box-shadow: 0 3px 8px rgba(0,0,0,0.25);
    overflow: hidden;
  }
  .accent-bar {
    position: absolute;
    left: 0;
    top: 182px;
    width: 22px;
    height: 72px;
    background: var(--navy);
  }
  .person { position: absolute; left: 52px; top: 176px; }
  .person-name {
    font-family: "Spectral", serif;
    font-weight: 500;
    font-size: 41px;
    line-height: 44px;
    color: var(--navy);
    text-transform: uppercase;
    letter-spacing: 0.5px;
  }
  .person-title {
    font-family: "Lato", sans-serif;
    font-size: 27px;
    line-height: 32px;
    color: var(--grey);
  }
  .address {
    position: absolute;
    left: 52px;
    top: 384px;
    font-family: "Montserrat", sans-serif;
    font-size: 24px;
    line-height: 31px;
    color: var(--grey);
  }
  .firm {
    position: absolute;
    left: 429px;
    width: 440px;
    top: 62px;
    display: flex;
    flex-direction: column;
    align-items: center;
  }
  .firm-mark {
    width: 72px;
    height: 72px;
    background: var(--navy);
  }
  .firm-name {
    margin-top: 44px;
    font-family: "Montserrat", sans-serif;
    font-weight: 400;
    font-size: 30px;
    line-height: 36px;
    letter-spacing: 3px;
    color: var(--navy);
    text-transform: uppercase;
    white-space: nowrap;
  }
  .contacts {
    position: absolute;
    left: 508px;
    top: 305px;
    list-style: none;
    font-family: "Montserrat", sans-serif;
    font-size: 26px;
    color: var(--grey);
  }
  .contacts li { display: flex; align-items: center; height: 37.5px; }
  .contacts svg { width: 26px; height: 26px; margin-right: 7px; fill: var(--navy); flex: none; }
  .stripe { position: absolute; left: 0; width: 100%; background: var(--navy); }
  .stripe-upper { top: 464px; height: 10px; }
  .stripe-lower { top: 484px; height: 10px; }
</style>
</head>
<body>
  <div class="card">
    <div class="accent-bar"></div>

    <div class="person">
      <div class="person-name">Paul Wexbury</div>
      <div class="person-title">Managing Partner</div>
    </div>

    <div class="firm">
      <div class="firm-mark"></div>
      <div class="firm-name">Quayvale Lawyers</div>
    </div>

    <div class="address">
      Level 9, 41 Tansy Lane<br>
      Sydney NSW 2000
    </div>

    <ul class="contacts">
      <li>
        <svg viewBox="0 0 24 24" aria-hidden="true"><path d="M2 7c0-2 3-4 10-4s10 2 10 4v2h-5V7.5c-1.5-.6-3-.8-5-.8s-3.5.2-5 .8V9H2z"/><path d="M5 11l2-3h10l2 3v10H5z"/><circle cx="12" cy="15" r="3" fill="#fbfbfb"/><circle cx="12" cy="15" r="1.4"/></svg>
        02 7346 2190
      </li>
      <li>
        <svg viewBox="0 0 24 24" aria-hidden="true"><path d="M7 1h10a2 2 0 0 1 2 2v18a2 2 0 0 1-2 2H7a2 2 0 0 1-2-2V3a2 2 0 0 1 2-2zm0 3v14h10V4zm5 15.5a1.2 1.2 0 1 0 0 2.4 1.2 1.2 0 0 0 0-2.4z"/></svg>
        02 6273 4415
      </li>
      <li>
        <svg viewBox="0 0 24 24" aria-hidden="true"><path d="M1 5h22v14H1zm2 2v.4l9 6.5 9-6.5V7zm0 2.9V17h18V9.9l-9 6.5z"/></svg>
        paul@qvlegal.com.au
      </li>
      <li>
        <svg viewBox="0 0 24 24" aria-hidden="true"><path d="M12 1a11 11 0 1 0 0 22 11 11 0 0 0 0-22zm-1 3c-1 1-3 1-3 3s2 1 3 3-1 3 0 5 2 3 1 5c-4-.5-8-4-8-9 0-3 2-6 7-7zm5 2c2 1 4 3 4 6-1 0-2-1-3 0s0 3-1 4-3 0-3-2 2-2 2-4-2-2-1-4z"/></svg>
        www.qvlegal.com.au
      </li>
    </ul>

    <div class="stripe stripe-upper"></div>
    <div class="stripe stripe-lower"></div>
  </div>
</body>
</html>
```